New funky, super creative logo design for printing business

Stamp, Wrap and Ship

We are a new digital printing business, based on the Gold Coast of Australia. We have a web site under construction - www.stampwrapandship.net, which will aim at the Business to Business market. We are digital printers, offering a wide variety of print products from business cards to wide format print jobs for consumers and small to medium sized business'. We offer up to date technological, digital and wide format print, at hi octane speed. Our prices are very competitive, and turnaround is super fast.

We like to think outside the box, and this should shine through in the design and colours that you use. Be bold and creative, we want to stand out from the crowd.

We will also soon be needing a full suite of marketing collaterals - posters, letterheads, scrap pads, calendars, banners etc. but this will come later, once we have decided on the logo and layouts.

We want a vibrant, bold image, communicating vibrancy and excitement.

Details on the card are company name: Stamp, Wrap and Ship.
www.stampwrapandship.net.
contact: Corinne (+61)437182265
e-mail:corinne@stampwrapandship.net

I must be able to change some of the details such as the name and number on the card.

Target Market(s)

Business to business, small retail, some individuals

Industry/Entity Type

Construction

Requirements
Must have
• Unique funky logo.
Nice to have
• A three dimensional look,with depth in the logo.

```html
<!DOCTYPE html>
<html lang="en">
<head>
<meta charset="utf-8">
<title>Stamp, Wrap and Ship — Folding Business Card</title>
<link href="https://fonts.googleapis.com/css2?family=Arimo:wght@400;700&display=swap" rel="stylesheet">
<style>
  :root {
    --backdrop: #f3f3f3;
    --card: #ffffff;
    --flap: #f7f7f7;
    --fold-line: #d4d4d4;
    --card-edge: #dcdcdc;
    --brand-green: #00ff00;
    --ink: #000000;
    --text: #1a1a1a;
  }
  * { box-sizing: border-box; margin: 0; padding: 0; }
  html, body {
    width: 1200px;
    height: 796px;
    overflow: hidden;
    background: var(--backdrop);
    font-family: "Arimo", Arial, sans-serif;
  }
  .stage { position: relative; width: 1200px; height: 796px; }

  .view-label {
    position: absolute;
    font-size: 18px;
    font-weight: 700;
    color: var(--ink);
    letter-spacing: 0.2px;
  }
  .view-label--folded { left: 124px; top: 227px; }
  .view-label--open { left: 486px; top: 227px; }

  .card-folded {
    position: absolute;
    left: 122px; top: 257px;
    width: 289px; height: 288px;
    background: var(--card);
    border: 1px solid var(--card-edge);
  }
  .card-folded__flap {
    position: absolute;
    right: 0; top: 0;
    width: 59px; height: 100%;
    background: var(--flap);
    border-left: 1px solid var(--fold-line);
    border-radius: 22px 0 0 22px;
  }

  .card-open {
    position: absolute;
    left: 483px; top: 257px;
    width: 619px; height: 289px;
    background: var(--card);
    border: 1px solid var(--card-edge);
    border-radius: 0 20px 20px 0;
  }
  .card-open__fold {
    position: absolute;
    top: 0; bottom: 0;
    width: 1px;
    background: var(--fold-line);
  }
  .card-open__fold--first { left: 289px; }
  .card-open__fold--second { left: 579px; }

  .brand-mark {
    position: absolute;
    width: 150px; height: 150px;
    background: var(--brand-green);
    display: flex;
    flex-direction: column;
    justify-content: center;
    padding-left: 14px;
  }
  .brand-mark__name {
    font-family: "Arimo", Arial, sans-serif;
    font-weight: 700;
    font-size: 25px;
    line-height: 1.05;
    color: var(--ink);
    text-transform: uppercase;
  }
  .card-folded .brand-mark { left: 50px; top: 67px; }
  .card-open .brand-mark { left: 33px; top: 24px; }

  .contact-block {
    position: absolute;
    left: 211px; top: 185px;
    font-size: 16px;
    line-height: 21.7px;
    color: var(--text);
    white-space: nowrap;
  }
</style>
</head>
<body>
  <main class="stage">
    <h2 class="view-label view-label--folded">Folded</h2>
    <section class="card-folded" aria-label="Folded card front">
      <div class="brand-mark">
        <p class="brand-mark__name">Stamp,<br>Wrap and<br>Ship</p>
      </div>
      <div class="card-folded__flap"></div>
    </section>

    <h2 class="view-label view-label--open">Open</h2>
    <section class="card-open" aria-label="Open card spread">
      <div class="brand-mark">
        <p class="brand-mark__name">Stamp,<br>Wrap and<br>Ship</p>
      </div>
      <span class="card-open__fold card-open__fold--first"></span>
      <span class="card-open__fold card-open__fold--second"></span>
      <address class="contact-block" style="font-style:normal">
        Stamp, Wrap and Ship.<br>
        www.stampwrapandship.net.<br>
        contact: Corinne (+61)437182265<br>
        e-mail:corinne@stampwrapandship.net
      </address>
    </section>
  </main>
</body>
</html>
```